Online Shop OSK

We need a web design for an online shop, called "OSK Boderl". The shop should layoutwise match with this head page: http://www.osk-bergluft.at/, as it is a partner page. So please use similar, matching colors like the red, blue, white. The shop is supposed to be a platform for a certain commerce region in Austria. It should be available for rural local stores like bakeries, liquor stores, butchers, regional grocery stores or traditional costume stores to offer their products in the online shop. The look should be simple, traditional, clear and matching to the Osk-bergluft page. If needed, you can google-search pictures of "Fuschlsee Salzburg" to use for background/banner etc. Others than that, pictures of food, traditional costumes (search word: austrian dirndl) are nice to be seen. Regarding Functions, the store will have the SAME functions as this page:http://www.velmora-markt.eu/ - using the "most famous" stores and its products for the starting page, going into detail pages by clicking these images. You can also think of a small area left for adverts of the local stores.

Target Market(s)

Target market are female as well as males, as well as families... Citizens of the countryside of this region in general as well as tourists of this region, looking online for individual local goods.

Industry/Entity Type

Shop

Requirements
Must have
• The design must have 3 pages: a starting page, a subsite with an overview for the different products of a certain store and a subsite with a product in detail.
• Please feel free to create some kind of a logo which is being used only online in the shop.
• Please think of the different "Stores" as categories, of different products of each store as the subpages and of a detailled description of one special product for the detail page.
Nice to have
• would be nice to have an emotional landscape image integrated in the design (such as you find for FUSCHLSEE SALZBURG in google) we dont have a proper picture yet.
Should not have
• the design should NOT look cheap or plain/technical. Emotions are of high importance as well as visual attraction for customers since we are selling good quality products of local stores and shops.

```html
<!DOCTYPE html>
<html lang="en">
<head>
<meta charset="utf-8">
<title>OSK Boderl – Shop</title>
<link rel="stylesheet" href="https://fonts.googleapis.com/css2?family=Arimo:wght@400;700&family=Vollkorn:wght@400;500&display=swap">
<style>
:root{
  --red:#e2001a;
  --nav-blue:#5d80ad;
  --head-blue:#6d8ab0;
  --foot-light:#8aa3c3;
  --foot-dark:#6484b0;
  --panel-line:#c8c8c8;
  --divider:#bdbdbd;
  --text-grey:#666;
  --price-grey:#6b6b6b;
  --page-bg:#ececec;
}
*{box-sizing:border-box;margin:0;padding:0}
html,body{width:1040px;height:1200px;overflow:hidden}
body{background:var(--page-bg);font-family:"Arimo",Arial,sans-serif;position:relative}
.page{position:absolute;left:21px;top:0;width:998px;height:1200px;background:#fff;box-shadow:0 0 6px rgba(0,0,0,.18)}
.topbar{position:absolute;left:0;top:0;width:100%;height:47px;background:linear-gradient(#fff 0,#f4f4f4 45%,#d9d9d9 100%);border-top:1px solid #ccc}
.topbar .service{position:absolute;right:30px;top:17px;font-size:11px;color:#111}
.header{position:absolute;left:0;top:47px;width:100%;height:79px;background:var(--head-blue)}
.brand{position:absolute;left:10px;top:14px;display:flex;align-items:center;gap:10px}
.brand .mark{width:22px;height:22px;background:var(--red)}
.brand .name{font-size:30px;font-weight:700;color:#fff;letter-spacing:.5px}
.banner{position:absolute;top:0;height:79px}
.banner.lake{left:268px;width:207px;background:linear-gradient(#b9cbe0,#7d9474 60%,#8fa7b9)}
.banner.plan{left:475px;width:200px;background:linear-gradient(135deg,#e7e9ec,#b8bdc4)}
.banner.kitchen{left:675px;width:130px;background:linear-gradient(#6d5a48,#c9c2b8)}
.banner.flower{left:805px;width:193px;background:radial-gradient(circle at 45% 50%,#f6f1d8 0,#e8e6dc 30%,#9ab06a 70%,#6f8a4a 100%)}
.nav{position:absolute;left:0;top:126px;width:100%;height:50px;background:var(--nav-blue);box-shadow:0 6px 8px -4px rgba(0,0,0,.35)}
.nav ul{list-style:none;position:absolute;left:195px;top:13px;display:flex;gap:24px}
.nav a{color:#fff;text-decoration:none;font-size:20px}
.nav .search{position:absolute;right:30px;top:15px}
.box{position:absolute;left:10px;width:199px;border:1px solid #bbb;border-radius:3px;background:#fff}
.box-title{background:var(--red);color:#fff;font-size:16px;height:46px;line-height:46px;padding-left:24px;border-radius:3px 3px 0 0}
.categories{top:208px;height:234px}
.categories ul{list-style:none;padding:10px 0 0 26px}
.categories li{font-size:14px;color:#444;line-height:29.5px}
.categories li::before{content:"› ";}
.cart{top:463px;height:194px}
.cart .box-title{height:37px;line-height:37px;padding-left:17px}
.cart .caret{display:inline-block;border:4px solid transparent;border-bottom:5px solid #fff;margin-left:6px;vertical-align:3px}
.cart .empty{font-size:9px;color:#666;padding:10px 0 0 11px}
.cart table{margin:8px 10px 0;width:177px;border-collapse:collapse;font-size:11px;color:#444}
.cart td{border:1px solid #e3e0da;background:#f6f4f0;height:27px;padding:0 9px}
.cart td.amount{text-align:right}
.cart .note{font-size:9px;color:#666;padding:9px 0 0 11px}
.cart .actions{display:flex;gap:4px;padding:14px 0 0 17px}
.cart .btn{background:var(--red);color:#fff;font-size:9px;height:23px;line-height:23px;text-align:center;border-radius:3px}
.ad{position:absolute;left:10px;width:199px;height:136px}
.ad.wine{top:677px;background:#ea2228}
.ad.cellar{top:832px;background:linear-gradient(160deg,#6a3a22,#2b1a12 60%,#4a2c1c)}
.catalogue{position:absolute;left:218px;top:209px;width:774px;height:843px;border:1px solid var(--panel-line);background:#fff}
.grid{position:absolute;left:13px;top:0;display:grid;grid-template-columns:repeat(3,231px);column-gap:29px}
.product{position:relative;height:285px;border-bottom:1px solid var(--divider)}
.product:nth-child(n+7){border-bottom:none}
.product:not(:nth-child(3n))::after{content:"";position:absolute;right:-15px;top:22px;height:212px;border-right:1px solid var(--divider)}
.bottle{position:absolute;left:50%;transform:translateX(-50%);bottom:122px;width:var(--w);height:var(--h);border-radius:8px 8px 4px 4px;background:var(--c)}
.product .title{position:absolute;left:30px;top:174px;font-size:19px;color:var(--text-grey)}
.product .buy{position:absolute;left:19px;top:206px;display:flex;align-items:center;gap:14px}
.price{font-family:"Vollkorn",Georgia,serif;font-size:23px;color:var(--price-grey);width:86px;text-align:right}
.buy-btn{background:var(--red);color:#fff;font-family:"Vollkorn",Georgia,serif;font-size:17px;width:90px;height:32px;line-height:32px;text-align:center;border-radius:3px}
.footer{position:absolute;left:0;top:1082px;width:100%;height:118px}
.footer .upper{height:56px;background:linear-gradient(#dde4ee 0,var(--foot-light) 10%,var(--foot-light) 100%);position:relative}
.footer .social{position:absolute;right:44px;top:21px;display:flex;gap:6px}
.footer .social span{width:18px;height:18px;border-radius:2px}
.footer .lower{height:62px;background:linear-gradient(90deg,#7e98bb,var(--foot-dark));position:relative;border-top:1px solid #a7b8cf}
.footer .brand{top:16px;left:10px}
.footer .copy{position:absolute;right:24px;top:30px;font-size:11px;font-weight:700;color:#fff}
</style>
</head>
<body>
<div class="page">
  <div class="topbar"><span class="service">Kontakt I Impressum</span></div>

  <header class="header">
    <div class="brand"><span class="mark"></span><span class="name">OSK Boderl</span></div>
    <div class="banner lake" role="img" aria-label="Mountain lake landscape"></div>
    <div class="banner plan" role="img" aria-label="Architectural floor plan"></div>
    <div class="banner kitchen" role="img" aria-label="Chefs in a kitchen"></div>
    <div class="banner flower" role="img" aria-label="Daisy flower close-up"></div>
  </header>

  <nav class="nav">
    <ul>
      <li><a href="#">Garments</a></li>
      <li><a href="#">Groceries</a></li>
      <li><a href="#">Liquors</a></li>
      <li><a href="#">Garment</a></li>
      <li><a href="#">Wine</a></li>
      <li><a href="#">Souvenir</a></li>
    </ul>
    <svg class="search" width="20" height="20" viewBox="0 0 20 20" aria-label="Search"><circle cx="8" cy="8" r="5.5" fill="none" stroke="#fff" stroke-width="2.6"/><line x1="12" y1="12" x2="18" y2="18" stroke="#fff" stroke-width="3" stroke-linecap="round"/></svg>
  </nav>

  <aside class="box categories">
    <div class="box-title">Categories</div>
    <ul>
      <li>Garments</li><li>Groceries</li><li>Liquors</li><li>Garment</li><li>Wine</li><li>Souvenir</li>
    </ul>
  </aside>

  <aside class="box cart">
    <div class="box-title">Cart<span class="caret"></span></div>
    <p class="empty">No products</p>
    <table>
      <tr><td>Shipping</td><td class="amount">$ 0.00</td></tr>
      <tr><td>Total</td><td class="amount">$ 0.00</td></tr>
    </table>
    <p class="note">Prices are tax excluded</p>
    <div class="actions"><span class="btn" style="width:71px">Cart</span><span class="btn" style="width:89px">Checkout</span></div>
  </aside>

  <div class="ad wine" role="img" aria-label="Wine discount advert for six or more bottles"></div>
  <div class="ad cellar" role="img" aria-label="Wine bottles in a cellar rack, best flavour advert"></div>

  <main class="catalogue">
    <div class="grid">
      <div class="product"><div class="bottle" role="img" aria-label="Bourbon bottle" style="--w:48px;--h:98px;--c:linear-gradient(90deg,#a84a14,#e08a3a,#9a3f10)"></div><p class="title">Lorem ipsum</p><div class="buy"><span class="price">$99.99</span><span class="buy-btn">Buy it!</span></div></div>
      <div class="product"><div class="bottle" role="img" aria-label="Clear spirit bottle with dark label" style="--w:28px;--h:120px;--c:linear-gradient(90deg,#c9cfc6,#f3f4ef,#b9c0b4)"></div><p class="title">Lorem ipsum</p><div class="buy"><span class="price">$89.99</span><span class="buy-btn">Buy it!</span></div></div>
      <div class="product"><div class="bottle" role="img" aria-label="Vodka bottle" style="--w:26px;--h:122px;--c:linear-gradient(90deg,#d8dde0,#fafafa,#cdd3d6)"></div><p class="title">Lorem ipsum</p><div class="buy"><span class="price">$49.99</span><span class="buy-btn">Buy it!</span></div></div>
      <div class="product"><div class="bottle" role="img" aria-label="Pisco bottle" style="--w:52px;--h:100px;--c:linear-gradient(90deg,#c9cdd2,#f5f5f3,#c0c5ca)"></div><p class="title">Lorem ipsum</p><div class="buy"><span class="price">$159.99</span><span class="buy-btn">Buy it!</span></div></div>
      <div class="product"><div class="bottle" role="img" aria-label="Tall clear vodka bottle" style="--w:22px;--h:122px;--c:linear-gradient(90deg,#d5dadd,#fbfbfb,#cfd4d7)"></div><p class="title">Lorem ipsum</p><div class="buy"><span class="price">$69.99</span><span class="buy-btn">Buy it!</span></div></div>
      <div class="product"><div class="bottle" role="img" aria-label="Clear vodka bottle" style="--w:40px;--h:126px;--c:linear-gradient(90deg,#bfc8cf,#f4f6f7,#b8c1c8)"></div><p class="title">Lorem ipsum</p><div class="buy"><span class="price">$99.99</span><span class="buy-btn">Buy it!</span></div></div>
      <div class="product"><div class="bottle" role="img" aria-label="Dark gift-wrapped bottle" style="--w:34px;--h:118px;--c:linear-gradient(#a8895a 0,#d9d3c6 25%,#222 60%,#111)"></div><p class="title">Lorem ipsum</p><div class="buy"><span class="price">$59.99</span><span class="buy-btn">Buy it!</span></div></div>
      <div class="product"><div class="bottle" role="img" aria-label="Dark gin bottle" style="--w:56px;--h:126px;--c:linear-gradient(90deg,#111,#3a3a3a,#111)"></div><p class="title">Lorem ipsum</p><div class="buy"><span class="price">$239.99</span><span class="buy-btn">Buy it!</span></div></div>
      <div class="product"><div class="bottle" role="img" aria-label="Whiskey bottle" style="--w:52px;--h:124px;--c:linear-gradient(90deg,#5a1a0c,#a8401c,#4a140a)"></div><p class="title">Lorem ipsum</p><div class="buy"><span class="price">$199.99</span><span class="buy-btn">Buy it!</span></div></div>
    </div>
  </main>

  <footer class="footer">
    <div class="upper">
      <div class="social"><span style="background:#3b5b98"></span><span style="background:#3fa9e0"></span><span style="background:#e8741f"></span></div>
    </div>
    <div class="lower">
      <div class="brand"><span class="mark"></span><span class="name">OSK Boderl</span></div>
      <p class="copy">© 2014 OSK Boderl Talregion</p>
    </div>
  </footer>
</div>
</body>
</html>
```